Web Design

We are Carvonta’s new and used car supermarket, we need a clean and nice look web design.

What included on homepage:
1. Logo
2. Slideshow (additional)
3. Menu - Home, About us, New cars, Used cars, Contact us
4. Advance Search
5. Customer Reviews
6. Social links - facebook, twitter , youtube
7. Banner Ads
8. Recent News
9. Newsletter

We just need psd files, home and contact us.

Industry/Entity Type

Used Car

Number of Pages Required

2 page

Requirements
Must have
• Webpage are well designed and in accordance with the color of the logo that is displayed in the file attachment.

```html
<!DOCTYPE html>
<html lang="en">
<head>
<meta charset="utf-8">
<title>Carvonta's Car Supermarket</title>
<link href="https://fonts.googleapis.com/css2?family=Open+Sans:ital,wght@0,400;0,600;0,700;0,800;1,400&family=Noto+Serif:ital@1&display=swap" rel="stylesheet">
<style>
:root{
  --blue:#0a5ea8;
  --blue-dark:#07498a;
  --red:#e8101c;
  --text:#555;
  --nav:#666;
  --panel:#e2e2e2;
  --foot-bg:#f1f2f3;
  --line:#d6d6d6;
  --white:#fff;
}
*{box-sizing:border-box;margin:0;padding:0}
html,body{width:958px;height:1200px;overflow:hidden;background:var(--white)}
body{position:relative;font-family:'Open Sans',sans-serif;color:var(--text)}
.abs{position:absolute}

/* header */
.brand{left:104px;top:38px;display:flex;align-items:center;gap:8px}
.brand-mark{width:14px;height:14px;background:var(--blue)}
.brand-name{font-size:20px;font-weight:600;color:var(--blue);line-height:1}
.main-nav{right:104px;top:42px;display:flex;gap:19px;font-size:14px;color:var(--nav);letter-spacing:.2px}

/* hero */
.hero{left:0;top:105px;width:958px;height:336px;background:linear-gradient(100deg,#8c8c8c 0%,#d9d9d9 35%,#efefef 55%,#9a9a9a 80%,#5c5c5c 100%)}
.hero-title{right:104px;top:32px;text-align:right;font-size:27px;font-weight:700;color:var(--white);line-height:34px;text-shadow:0 1px 3px rgba(0,0,0,.4)}
.dots{right:104px;top:106px;display:flex;gap:8px}
.dots span{width:11px;height:11px;border-radius:50%;background:var(--white)}
.dots .on{background:var(--red)}
.arrow{top:124px;width:32px;height:67px;background:rgba(240,240,240,.92);display:flex;align-items:center;justify-content:center}

/* welcome */
.welcome{left:102px;top:476px;width:492px}
.welcome h1{font-size:19.5px;font-weight:400;color:var(--blue);margin-bottom:10px;white-space:nowrap}
.welcome p{font-size:11.3px;line-height:14.5px;margin-bottom:8px}

/* search */
.search{left:614px;top:468px;width:240px;height:144px;border-radius:3px;background:linear-gradient(#0b68b8,#0a5ea8 60%,#074d92)}
.search h2{height:30px;padding:8px 17px;font-size:13px;font-weight:600;color:var(--white);background:var(--blue-dark);border-radius:3px 3px 0 0}
.select{position:absolute;left:17px;width:194px;height:24px;background:var(--white);border-radius:2px;font-size:8.5px;font-style:italic;color:#777;padding:6px 10px}
.select::after{content:"";position:absolute;right:9px;top:9px;border:4px solid transparent;border-top:5px solid #333}
.search-btn{position:absolute;left:17px;top:110px;width:46px;height:18px;background:var(--red);border:1px solid var(--white);border-radius:3px;color:var(--white);font-size:6.5px;font-weight:600;text-align:center;line-height:16px}

/* tabs + cars */
.tabs{left:102px;top:644px;width:492px;height:25px;border-bottom:1px solid var(--line);display:flex;font-size:13px;color:var(--blue)}
.tabs span{margin-right:40px}
.tabs .active{position:relative;border-bottom:2px solid var(--red);height:25px}
.car{width:130px;height:86px;border:2px solid #ddd;border-radius:2px;background:var(--white)}
.car-photo{height:72px;margin:2px 6px 0}
.car-bar{position:absolute;left:0;right:0;bottom:0;height:10px;background:#8a8a8a;color:var(--white);font-size:6px;line-height:10px;text-align:center}
.banner-ad{left:615px;top:648px;width:240px;height:239px;background:var(--panel);padding:50px 0 0 14px;font-size:15.5px;color:#555;white-space:nowrap}

/* lower section */
.lower{left:0;top:920px;width:958px;height:230px;background:var(--foot-bg)}
.col-title{font-size:19px;color:var(--blue);font-weight:400}
.divider{top:37px;width:1px;height:144px;background:#ccc}
.quote{left:116px;top:60px;width:180px;height:68px;background:var(--white);border:1px solid #ddd;border-bottom:2px solid var(--blue);border-radius:4px;padding:12px 10px 0 26px;font-family:'Noto Serif',serif;font-style:italic;font-weight:400;font-size:7px;line-height:12px;color:#666}
.quote-mark{position:absolute;left:10px;top:8px;color:var(--red);font-size:16px}
.avatar{left:136px;top:148px;width:20px;height:20px;border-radius:50%;background:linear-gradient(#d8b090,#8a6a55)}
.small-link{font-size:7.5px;font-style:italic;color:#666;text-decoration:underline}
.news{left:399px;width:192px}
.date{position:absolute;left:0;top:0;width:35px;height:32px;background:var(--white);border:1px solid #ddd;text-align:center}
.date b{display:block;background:var(--red);color:var(--white);font-size:9px;font-weight:400;line-height:12px}
.date i{font-style:normal;font-size:13px;font-weight:600;color:var(--blue);line-height:18px}
.news h3{margin-left:48px;font-size:11.5px;font-weight:600;color:#555}
.news p{margin-left:48px;font-size:6px;line-height:9.5px;color:#666;margin-top:4px}
.news p em{font-style:normal;color:var(--blue)}
.signup{left:684px;top:1004px;width:166px;height:24px;border:2px solid #ddd;border-radius:4px;background:var(--white);font-size:8.5px;font-style:italic;color:#999;padding:5px 20px}
.signup-btn{position:absolute;right:-2px;top:-2px;width:38px;height:24px;background:var(--red);border-radius:0 4px 4px 0;display:flex;align-items:center;justify-content:center}
.social{top:1092px;width:24px;height:24px;border-radius:2px}

/* footer */
.footer{left:0;top:1150px;width:958px;height:50px;background:var(--blue);color:var(--white)}
.footer-nav{left:103px;top:17px;display:flex;gap:17px;font-size:12px}
.copyright{right:104px;top:20px;font-size:9px}
</style>
</head>
<body>

<header>
  <div class="abs brand">
    <span class="brand-mark"></span>
    <span class="brand-name">Carvonta's Car Supermarket</span>
  </div>
  <nav class="abs main-nav"><span>HOME</span><span>ABOUT US</span><span>NEW CARS</span><span>USED CARS</span><span>CONTACT US</span></nav>
</header>

<section class="abs hero" role="img" aria-label="Slideshow photo of a white sports car parked in a bright showroom garage">
  <h2 class="abs hero-title">LOREM IPSUM DOLOR SIT<br>AMET CONSECTETUR</h2>
  <div class="abs dots"><span></span><span class="on"></span><span></span><span></span></div>
  <div class="abs arrow" style="left:0"><svg width="14" height="22" viewBox="0 0 14 22"><path d="M11 2 3 11l8 9" fill="none" stroke="#333" stroke-width="4"/></svg></div>
  <div class="abs arrow" style="right:0"><svg width="14" height="22" viewBox="0 0 14 22"><path d="M3 2l8 9-8 9" fill="none" stroke="#333" stroke-width="4"/></svg></div>
</section>

<section class="abs welcome">
  <h1>WELCOME TO CARVONTA'S CAR SUPERMARKET</h1>
  <p>Lorem ipsum dolor sit amet, consectetur adipisicing elit, sed do eiusmod tempor incididunt ut labore et dolore magna aliqua. Ut enim ad minim veniam, quis nostrud exercitation ullamco laboris nisi ut aliquip ex ea commodo consequat.</p>
  <p>Duis aute irure dolor in reprehenderit in voluptate velit esse cillum dolore eu fugiat nulla pariatur. Excepteur sint occaecat cupidatat non proident, sunt in culpa qui officia deserunt mollit anim id est laborum.</p>
</section>

<section class="abs search">
  <h2>SEARCH CARS</h2>
  <div class="select" style="top:45px">Select model</div>
  <div class="select" style="top:76px">Select manufacturer</div>
  <div class="search-btn">Search Now</div>
</section>

<nav class="abs tabs"><span class="active">Featured</span><span>Latest</span><span>Popular</span><span>Most Viewed</span></nav>

<div class="abs car" style="left:102px;top:693px"><div class="car-photo" role="img" aria-label="Blue sports car" style="background:radial-gradient(ellipse at center,#2e7fc4 0%,#9cc3e4 45%,#fff 70%)"></div><div class="car-bar">VIEW DETAILS &nbsp;&nbsp;➔</div></div>
<div class="abs car" style="left:277px;top:693px"><div class="car-photo" role="img" aria-label="Silver coupe" style="background:radial-gradient(ellipse at center,#8d9197 0%,#cfd2d6 45%,#fff 70%)"></div><div class="car-bar">VIEW DETAILS &nbsp;&nbsp;➔</div></div>
<div class="abs car" style="left:452px;top:693px"><div class="car-photo" role="img" aria-label="Red sports car with white stripes" style="background:radial-gradient(ellipse at center,#d8141c 0%,#f0a0a0 45%,#fff 70%)"></div><div class="car-bar">VIEW DETAILS &nbsp;&nbsp;➔</div></div>
<div class="abs car" style="left:102px;top:801px"><div class="car-photo" role="img" aria-label="Orange sports car with white stripes" style="background:radial-gradient(ellipse at center,#f07a10 0%,#f8c490 45%,#fff 70%)"></div><div class="car-bar">VIEW DETAILS &nbsp;&nbsp;➔</div></div>
<div class="abs car" style="left:277px;top:801px"><div class="car-photo" role="img" aria-label="Yellow coupe" style="background:radial-gradient(ellipse at center,#f2d820 0%,#f8ec9a 45%,#fff 70%)"></div><div class="car-bar">VIEW DETAILS &nbsp;&nbsp;➔</div></div>
<div class="abs car" style="left:452px;top:801px"><div class="car-photo" role="img" aria-label="Dark blue sports car" style="background:radial-gradient(ellipse at center,#0c3e9a 0%,#8aa6d8 45%,#fff 70%)"></div><div class="car-bar">VIEW DETAILS &nbsp;&nbsp;➔</div></div>

<aside class="abs banner-ad">Your Banner AD Goes Here</aside>

<section class="abs lower">
  <h2 class="abs col-title" style="left:116px;top:14px">Testimonials</h2>
  <h2 class="abs col-title" style="left:399px;top:14px">Recent News</h2>
  <h2 class="abs col-title" style="left:683px;top:14px">Newsletter</h2>
  <div class="abs divider" style="left:347px"></div>
  <div class="abs divider" style="left:641px"></div>

  <div class="abs quote"><span class="quote-mark">“</span>Lorem ipsum dolor sit amet, consec tetur adipisicing elit, sed do eiusmod tempor incididunt ut labore.</div>
  <svg class="abs" style="left:136px;top:127px" width="22" height="14"><path d="M0 0h22L11 13z" fill="#fff" stroke="#0a5ea8" stroke-width="1.5"/><path d="M1 0h20" stroke="#fff" stroke-width="2"/></svg>
  <div class="abs avatar" role="img" aria-label="Customer portrait"></div>
  <div class="abs" style="left:166px;top:156px;font-size:7.5px;color:var(--blue)">Mark Ellison, New York</div>
  <div class="abs small-link" style="left:116px;top:190px">View More</div>

  <article class="abs news" style="top:55px"><div class="date"><b>Aug</b><i>15</i></div><h3>Adipisicing elit sed</h3><p>Eiusmod tempor incididunt ut labore et dolore magna aliqua. Ut enim ad minim veniam, quis nostrud exercitation ullam...<em>[Read More]</em></p></article>
  <div class="abs" style="left:399px;top:114px;width:192px;height:1px;background:#ddd"></div>
  <article class="abs news" style="top:137px"><div class="date"><b>Aug</b><i>15</i></div><h3>Adipisicing elit sed</h3><p>Eiusmod tempor incididunt ut labore et dolore magna aliqua. Ut enim ad minim veniam, quis nostrud exercitation ullam...<em>[Read More]</em></p></article>
  <div class="abs small-link" style="left:400px;top:190px">View More</div>

  <p class="abs" style="left:684px;top:48px;font-size:9.5px;line-height:14.5px;color:#444">Sign up to receive daily updates<br>and news from Carvonta's</p>
  <h2 class="abs col-title" style="left:683px;top:134px">Keep Connected</h2>
</section>

<div class="abs signup">Enter your Email
  <div class="signup-btn"><svg width="16" height="12" viewBox="0 0 16 12"><path d="M1 6h12M8 1l5 5-5 5" fill="none" stroke="#fff" stroke-width="2.4"/></svg></div>
</div>
<div class="abs social" style="left:685px;background:#1ea1e8" aria-label="Social network link 1"></div>
<div class="abs social" style="left:723px;background:#c4161c" aria-label="Social network link 2"></div>
<div class="abs social" style="left:762px;background:#3b5ca8" aria-label="Social network link 3"></div>
<div class="abs social" style="left:800px;background:#e2472f" aria-label="Social network link 4"></div>

<footer class="abs footer">
  <nav class="abs footer-nav"><span>Home</span><span>About us</span><span>New cars</span><span>Used cars</span><span>Contact us</span></nav>
  <div class="abs copyright">Copyright©carvontacarsupermarket2014. All Rights Reserved</div>
</footer>

</body>
</html>
```